Sports Psychology Business Card Design

Need a catchy and unique business card design for our sport psychology practice. We provide mental performance counseling and consulting to performers from all types of industries with a special emphases on athletes.The name of our practice is "Steady Core of Achievement" or "SCA" as is indicated in the logo examples submitted in this brief. Also provided were logos with specific sports referenced which represent sources of our clients from those sports.

Target Market(s)

Executives, Professionals (doctors, lawyers, etc.), Athletes, Entertainers and other performers

Contact Information for Business Card

Need to include our logo (logos provided in this brief).

Font styles to use
Other font styles liked:
• Font can be found in logo

Colors
0792cd
34a7d8
85cae6

Requirements
Must have
• Our logo and reference to our provision of mental performance counseling/consulting/coaching
Nice to have
• References to sports that our athletes play as provided in the brief.
Should not have
• This is not a general wellness consulting practice. Our focus is on consulting to improve mental performance.

```html
<!DOCTYPE html>
<html lang="en">
<head>
<meta charset="utf-8">
<title>Steady Core of Achievement — Business Cards</title>
<link href="https://fonts.googleapis.com/css2?family=Orbitron:wght@800&family=Montserrat:wght@400;500;600&display=swap" rel="stylesheet">
<style>
  :root {
    --stage: #e9edee;
    --card: #ffffff;
    --blue-deep: #0a6fc2;
    --blue-mid: #0792cd;
    --blue-light: #85cae6;
    --ink: #1c1f22;
    --text-grey: #55595c;
    --badge-line: #d5d8da;
    --badge-fill: #f4f5f6;
  }
  * { box-sizing: border-box; margin: 0; padding: 0; }
  html, body { width: 1200px; height: 900px; overflow: hidden; }
  body {
    background: var(--stage);
    font-family: "Montserrat", sans-serif;
    position: relative;
  }
  .card {
    position: absolute;
    width: 490px;
    height: 280px;
    background: var(--card);
    box-shadow: 0 10px 26px rgba(0,0,0,0.10), 0 2px 4px rgba(0,0,0,0.06);
  }
  .card--brand { left: 80px; top: 90px; }
  .card--contact { left: 630px; top: 90px; }
  .card--tagline { left: 355px; top: 500px; }

  /* Brand side: name placeholder where the mark stands */
  .brand-name {
    position: absolute;
    left: 0; right: 0; top: 96px;
    text-align: center;
    font-family: "Montserrat", sans-serif;
    font-weight: 600;
    font-size: 48px;
    letter-spacing: 6px;
    color: var(--ink);
  }
  .brand-url {
    position: absolute; right: 28px; bottom: 24px;
    font-size: 13px; color: var(--text-grey); letter-spacing: 0.5px;
  }

  /* Contact side */
  .contact { position: absolute; left: 40px; top: 50px; right: 30px; }
  .contact__name {
    font-family: "Orbitron", sans-serif;
    font-weight: 800; font-size: 25px;
    color: var(--blue-deep); letter-spacing: 1px;
  }
  .contact__role {
    font-size: 12.5px; font-weight: 500; letter-spacing: 1.6px;
    color: var(--ink); margin-top: 6px;
  }
  .contact__list { list-style: none; margin-top: 30px; }
  .contact__item {
    display: flex; gap: 10px;
    font-size: 12.5px; color: var(--text-grey);
    line-height: 1.55; margin-bottom: 10px;
  }
  .contact__label { font-weight: 500; color: var(--ink); width: 16px; flex: none; }

  /* Tagline side: full name placeholder in one colour and weight */
  .tagline {
    position: absolute; left: 42px; right: 42px; top: 52px;
    font-family: "Montserrat", sans-serif; font-weight: 600;
    font-size: 30px; line-height: 1.25; letter-spacing: 1px;
    color: var(--blue-mid);
  }
  .sport-badges {
    position: absolute; left: 42px; right: 42px; bottom: 36px;
    display: flex; gap: 16px;
  }
  .sport-badge {
    flex: 1; height: 48px;
    border: 1px solid var(--badge-line);
    background: var(--badge-fill);
  }
</style>
</head>
<body>
  <section class="card card--brand" aria-label="Card brand side">
    <p class="brand-name">SCA</p>
    <p class="brand-url">www.steadycore.co</p>
  </section>

  <section class="card card--contact" aria-label="Card contact side">
    <div class="contact">
      <h1 class="contact__name">DANA WHITLOCK</h1>
      <p class="contact__role">MENTAL PERFORMANCE CONSULTANT</p>
      <ul class="contact__list">
        <li class="contact__item"><span class="contact__label">A.</span><span>Lorem ipsum dolor sit amet, consect etuer<br>adipiscing elit, sed diam nonummy</span></li>
        <li class="contact__item"><span class="contact__label">E.</span><span>dana@steadycore.co</span></li>
        <li class="contact__item"><span class="contact__label">T.</span><span>555-014-2290</span></li>
      </ul>
    </div>
  </section>

  <section class="card card--tagline" aria-label="Card tagline side">
    <p class="tagline">THE STEADY CORE<br>OF ACHIEVEMENT</p>
    <div class="sport-badges">
      <div class="sport-badge" role="img" aria-label="Sport badge"></div>
      <div class="sport-badge" role="img" aria-label="Sport badge"></div>
      <div class="sport-badge" role="img" aria-label="Sport badge"></div>
    </div>
  </section>
</body>
</html>
```